Business Card Design Project

Use our current logo. Clean design.

Industry/Entity Type

Business

Requirements
Must have
• Marisela DUBRANCQ
M. Law
Managing Partner

Alpenvorsa AG
Kornhalmweg 214
CH-3097 Liebefeld

M. +41 79 412 56 27
T. +41 31 928 44 10
F. +41 31 928 44 19

m.dubrancq@alpenvorsa-example.com
www.alpenvorsa-example.com

```html
<!DOCTYPE html>
<html lang="de">
<head>
<meta charset="utf-8">
<title>Alpenvorsa AG – Visitenkarte</title>
<link href="https://fonts.googleapis.com/css2?family=Roboto+Slab:wght@300;400;700&display=swap" rel="stylesheet">
<style>
  :root {
    --backdrop: #e6e4e5;
    --card-light: #fbfbfb;
    --card-dark: #585656;
    --ink-dark: #3e3c3d;
    --ink-light: #f4f4f4;
    --ink-soft: #dcdcdc;
  }
  * { margin: 0; padding: 0; box-sizing: border-box; }
  html, body {
    width: 1200px;
    height: 900px;
    overflow: hidden;
    background: var(--backdrop);
    font-family: "Roboto Slab", Georgia, serif;
  }
  .canvas {
    position: relative;
    width: 1200px;
    height: 900px;
  }
  .card {
    position: absolute;
    top: 302px;
    width: 520px;
    height: 297px;
    border-radius: 2px;
    box-shadow: 0 10px 24px rgba(0,0,0,0.12), 0 2px 4px rgba(0,0,0,0.08);
  }
  .card--front {
    left: 50px;
    background: var(--card-light);
    display: flex;
    align-items: center;
    justify-content: center;
  }
  .company-name {
    color: var(--ink-dark);
    font-weight: 400;
    font-size: 26px;
  }
  .card--back {
    left: 630px;
    background: var(--card-dark);
    color: var(--ink-light);
    font-size: 13px;
    line-height: 17px;
  }
  .holder {
    position: absolute;
    top: 40px;
    right: 36px;
  }
  .holder__name {
    font-weight: 700;
    font-size: 15px;
    line-height: 19px;
  }
  .holder__title {
    font-weight: 300;
    font-size: 11px;
    line-height: 15px;
    color: var(--ink-soft);
  }
  .contact {
    position: absolute;
    left: 36px;
    top: 100px;
  }
  .contact__address,
  .contact__phones {
    font-weight: 300;
    margin-bottom: 12px;
  }
  .contact__phones b { font-weight: 700; }
  .contact__web { font-weight: 300; }
</style>
</head>
<body>
<main class="canvas">
  <section class="card card--front" aria-label="Vorderseite">
    <p class="company-name">Alpenvorsa</p>
  </section>

  <section class="card card--back" aria-label="Rückseite">
    <div class="holder">
      <p class="holder__name">Marisela DUBRANCQ</p>
      <p class="holder__title">M. Law / Managing Partner</p>
    </div>
    <div class="contact">
      <p class="contact__address">Alpenvorsa AG<br>Kornhalmweg 214<br>CH-3097 Liebefeld</p>
      <p class="contact__phones">
        <b>M.</b> +41 79 412 56 27<br>
        <b>T.</b> +41 31 928 44 10<br>
        <b>F.</b> +41 31 928 44 19
      </p>
      <p class="contact__web">m.dubrancq@alpenvorsa-example.com<br>www.alpenvorsa-example.com</p>
    </div>
  </section>
</main>
</body>
</html>
```